Velnora - Quality health delivered at your door

Velnora offers home and Community Based Services for adults who wish to continue live independently in their communities. We increase accessibility to health care, reduce health care delivery gap, reduce mortality and morbidity, reduce health while promoting healthy living in the comfort of our patients communities or homes.

We provide on site services and deliver high quality healthcare at your door. Our experienced physicians coordinate care with our certified nurse practitioners and provide chronic care management, physical therapy, rehabilitation and medications management.

Target Market(s)

Older population living in independent living facilities

Industry/Entity Type

Health Care

Contact Information for Business Card

Velnora

Number of Pages Required

4 page

Font styles to use
Sans Serif

Colors

Designer to choose colors to be used in the design.

```html
<!DOCTYPE html>
<html lang="en">
<head>
<meta charset="utf-8">
<title>Velnora - Quality health delivered at your door</title>
<link rel="stylesheet" href="https://fonts.googleapis.com/css2?family=Marcellus&family=Open+Sans:wght@400;600;700&display=swap">
<style>
:root{
  --orange:#f7941d;
  --green:#5d7d1c;
  --lime:#7cb518;
  --dark:#333333;
  --footer:#3a3a3a;
  --light:#f1f1f1;
  --text:#333;
  --muted:#888;
  --white:#fff;
}
*{box-sizing:border-box;margin:0;padding:0}
html,body{width:1200px;height:3114px;overflow:hidden}
body{font-family:"Open Sans",Arial,sans-serif;color:var(--text);background:var(--white);position:relative}
.display{font-family:"Marcellus",Georgia,serif;font-weight:400}
.top-band{height:36px;background:var(--orange)}
.header{height:109px;background:#f4f4f4;position:relative}
.header-info{position:absolute;top:28px;display:flex;gap:14px;font-size:12px;line-height:17px;color:#555}
.header-info strong{display:block;font-size:14px;color:#333;margin-bottom:2px}
.hours{left:64px}
.address{left:912px}
.brand{position:absolute;left:50%;top:-24px;transform:translateX(-50%);text-align:center}
.brand-dot{width:98px;height:98px;border-radius:50%;background:var(--white);border:6px solid var(--orange);margin:0 auto}
.brand-name{font-family:"Marcellus",Georgia,serif;font-size:30px;color:var(--green);margin-top:2px;letter-spacing:1px}
.nav{height:54px;background:var(--dark);display:flex;justify-content:space-between;align-items:center;padding:0 58px}
.nav a{color:var(--white);font-size:13px;text-decoration:none;font-weight:600}
.hero{height:586px;position:relative;background:linear-gradient(100deg,#cfc8b4 0%,#e6e2d6 40%,#7ebdb5 62%,#e4b9b5 85%,#d8d4c9 100%)}
.hero-copy{position:absolute;left:64px;top:170px}
.tag{display:inline-block;color:var(--white);font-family:"Marcellus",Georgia,serif;padding:2px 10px}
.tag-orange{background:var(--orange);font-size:30px}
.tag-green{background:var(--lime);font-size:40px;margin-top:4px}
.hero-copy p{color:#222;font-size:16px;line-height:22px;margin-top:20px;width:480px}
.btn-dark{display:inline-block;margin-top:18px;background:#222;color:var(--white);font-size:15px;padding:6px 20px;border-radius:5px}
.about{position:absolute;left:68px;top:752px;width:1066px;height:338px;background:var(--light);text-align:center;padding-top:30px}
h2{font-size:40px;letter-spacing:1px;color:#111}
.rule{width:60px;height:3px;background:var(--green);margin:14px auto 0}
.about p{font-size:16px;line-height:28px;color:#333;width:990px;margin:20px auto 0}
.btn-out{display:inline-block;border:2px solid #ccc;border-radius:22px;font-size:12px;font-weight:700;padding:8px 34px;color:#333;background:var(--white)}
.about .btn-out{margin-top:26px}
.services-title{position:absolute;top:1152px;width:100%;text-align:center}
.services-photo{position:absolute;left:91px;top:1270px;width:432px;height:385px;background:linear-gradient(120deg,#d9e4d2,#b7cfa9 50%,#e9e6e0)}
.services-list{position:absolute;left:571px;top:1270px;width:560px;font-size:13px;line-height:21px}
.services-list ul{list-style:none;margin-top:14px}
.services-list li{display:flex;align-items:flex-start;gap:10px;margin-bottom:7px}
.services-list svg{flex:none;margin-top:4px}
.grid{position:absolute;top:1723px;left:0;width:1200px;height:478px}
.tile{position:absolute;height:239px;text-align:center;padding-top:22px}
.tile h3{font-family:"Marcellus",Georgia,serif;font-weight:400;font-size:26px;margin-top:6px}
.tile p{font-size:13px;line-height:20px;width:250px;margin:8px auto 0}
.tile .btn-out{margin-top:14px;padding:5px 28px;font-weight:400;font-size:13px}
.t-light{background:var(--light)}
.t-orange{background:var(--orange);color:var(--white)}
.t-green{background:var(--green);color:var(--white)}
.t-orange .btn-out,.t-green .btn-out{background:transparent;border-color:var(--white);color:var(--white)}
.blog-title{position:absolute;top:2240px;width:100%;text-align:center}
.blog-title .rule{background:#8fc5d0}
.card{position:absolute;top:2358px;width:241px}
.card-img{height:239px;border:2px solid #b6d36a}
.card h4{font-size:15px;font-weight:600;line-height:22px;margin-top:16px}
.meta{font-size:11px;color:var(--muted);font-style:italic;margin-top:12px}
.card p{font-size:11px;line-height:20px;color:var(--muted);margin-top:10px}
.card .btn-out{margin-top:18px;padding:6px 30px;font-size:11px}
.footer{position:absolute;top:2823px;left:0;width:1200px;height:291px;background:var(--footer);text-align:center;color:var(--white)}
.footer .brand-dot{width:80px;height:80px;border:4px solid var(--white);background:#555;margin-top:30px}
.footer .brand-name{color:var(--white);font-size:26px}
.footer-links{font-size:12px;margin-top:24px;font-weight:600}
.footer-links span{margin:0 8px}
.copy{font-size:12px;margin-top:14px}
.social{display:flex;justify-content:center;gap:24px;margin-top:22px}
.social i{width:26px;height:26px;background:#111;transform:rotate(45deg);display:block}
</style>
</head>
<body>
<div class="top-band"></div>
<header class="header">
  <div class="header-info hours">
    <svg width="26" height="26" viewBox="0 0 26 26"><circle cx="13" cy="14" r="10" fill="none" stroke="#7a9a2a" stroke-width="2.5"/><path d="M13 8v6l4 3" fill="none" stroke="#7a9a2a" stroke-width="2.5"/></svg>
    <div><strong>Opening Hours</strong>Monday to Friday | 8:30am to 5:30pm<br>Saturday | 8:30am to 4pm</div>
  </div>
  <div class="brand"><div class="brand-dot"></div><div class="brand-name">VELNORA</div></div>
  <div class="header-info address">
    <svg width="22" height="30" viewBox="0 0 22 30"><path d="M11 1C5 1 1 5.5 1 11c0 7 10 18 10 18s10-11 10-18C21 5.5 17 1 11 1z" fill="#5d7d1c"/><circle cx="11" cy="11" r="4" fill="#fff"/></svg>
    <div><strong>Address</strong>48 Harlow Lane Brookfield,<br>QLD 4069</div>
  </div>
</header>
<nav class="nav">
  <a>Assisted Living</a><a>Skilled Nursing</a><a>Independent Living</a><a>Services</a><a>Respite Care</a><a>Rehabilitation</a><a>Renew Learning</a><a>Center</a><a>Renew Learning®</a>
</nav>
<section class="hero" role="img" aria-label="Photo of a nurse caring for a smiling elderly woman in a bright room">
  <div class="hero-copy">
    <span class="tag tag-orange">We Provide Total</span><br>
    <span class="tag tag-green">Health Care Solution</span>
    <p>Every day we bring hope to millions of children in the world's hardest places as a sign of God's unconditional love.</p>
    <span class="btn-dark">Read More</span>
  </div>
</section>
<section class="about">
  <h2 class="display">ABOUT VELNORA</h2>
  <div class="rule"></div>
  <p>Velnora offers home and Community Based Services for adults who wish to continue to live independently in the comfort of their communities.</p>
  <p>We provide on site services and deliver high quality healthcare at your door. Our experienced physicians coordinate care with our certified nurse practitioners and provide chronic care management, physical therapy, rehabilitation and medications management.</p>
  <span class="btn-out">READ MORE</span>
</section>
<div class="services-title"><h2 class="display">OUR SERVICES</h2><div class="rule"></div></div>
<div class="services-photo" role="img" aria-label="Photo of a doctor holding hands with an elderly patient at a table"></div>
<div class="services-list">
  <p>Velnora offers home and Community Based Services for adults who wish to continue to live independently in the comfort of their communities.</p>
  <ul>
    <li><svg width="14" height="12" viewBox="0 0 14 12"><path d="M1 6l4 4 8-9" fill="none" stroke="#222" stroke-width="2.5"/></svg>Comprehensive primary care services</li>
    <li><svg width="14" height="12" viewBox="0 0 14 12"><path d="M1 6l4 4 8-9" fill="none" stroke="#222" stroke-width="2.5"/></svg>Coordination of specialty care</li>
    <li><svg width="14" height="12" viewBox="0 0 14 12"><path d="M1 6l4 4 8-9" fill="none" stroke="#222" stroke-width="2.5"/></svg>Chronic disease management such as COPD, Asthma, Diabetes mellitus, Heart disease like congestive heart failure, Alzheimer's dementia, etc...</li>
    <li><svg width="14" height="12" viewBox="0 0 14 12"><path d="M1 6l4 4 8-9" fill="none" stroke="#222" stroke-width="2.5"/></svg>Transitional Care</li>
    <li><svg width="14" height="12" viewBox="0 0 14 12"><path d="M1 6l4 4 8-9" fill="none" stroke="#222" stroke-width="2.5"/></svg>Skilled nursing visits for wound care, catheter care, ostomy</li>
    <li><svg width="14" height="12" viewBox="0 0 14 12"><path d="M1 6l4 4 8-9" fill="none" stroke="#222" stroke-width="2.5"/></svg>Social services assessment</li>
    <li><svg width="14" height="12" viewBox="0 0 14 12"><path d="M1 6l4 4 8-9" fill="none" stroke="#222" stroke-width="2.5"/></svg>Home health assistance</li>
    <li><svg width="14" height="12" viewBox="0 0 14 12"><path d="M1 6l4 4 8-9" fill="none" stroke="#222" stroke-width="2.5"/></svg>Physical therapy</li>
    <li><svg width="14" height="12" viewBox="0 0 14 12"><path d="M1 6l4 4 8-9" fill="none" stroke="#222" stroke-width="2.5"/></svg>Mental health</li>
    <li><svg width="14" height="12" viewBox="0 0 14 12"><path d="M1 6l4 4 8-9" fill="none" stroke="#222" stroke-width="2.5"/></svg>Dental health</li>
    <li><svg width="14" height="12" viewBox="0 0 14 12"><path d="M1 6l4 4 8-9" fill="none" stroke="#222" stroke-width="2.5"/></svg>Transportation</li>
  </ul>
</div>
<section class="grid">
  <div class="tile" style="left:0;top:0;width:600px;background:linear-gradient(120deg,#6f8a5a,#cfd6c6 45%,#9fb38a)" role="img" aria-label="Photo of a family with a dog sitting on a lawn"></div>
  <div class="tile t-light" style="left:600px;top:0;width:301px">
    <svg width="36" height="40" viewBox="0 0 36 40"><circle cx="18" cy="10" r="8" fill="#333"/><path d="M3 39c0-10 7-16 15-16s15 6 15 16z" fill="#333"/></svg>
    <h3>Clinicians</h3>
    <p>Dana Whitfield LCSW, M.Ed has over fifteen 12 years of experience working in the mental health field.</p>
    <span class="btn-out">Read More</span>
  </div>
  <div class="tile t-orange" style="left:901px;top:0;width:299px">
    <svg width="40" height="40" viewBox="0 0 40 40"><path d="M9 4l7 7-4 4c2 5 6 9 11 11l4-4 7 7-5 5C18 34 6 22 4 9z" fill="#fff"/><path d="M24 4a12 12 0 0 1 12 12M24 10a6 6 0 0 1 6 6" fill="none" stroke="#fff" stroke-width="2.5"/></svg>
    <h3>Phone Coaching</h3>
    <p>For Colorado families living in an area where there are few or no attachment and trauma competent clinicians</p>
    <span class="btn-out">Read More</span>
  </div>
  <div class="tile t-light" style="left:0;top:239px;width:301px">
    <svg width="44" height="40" viewBox="0 0 44 40"><circle cx="22" cy="9" r="7" fill="#333"/><circle cx="8" cy="20" r="5" fill="#333"/><circle cx="36" cy="20" r="5" fill="#333"/><rect x="14" y="20" width="16" height="18" rx="3" fill="#333"/></svg>
    <h3>Insurance</h3>
    <p>Dana Whitfield LCSW, M.Ed has over fifteen 12 years of experience working in the mental health field.</p>
    <span class="btn-out">Read More</span>
  </div>
  <div class="tile t-green" style="left:301px;top:239px;width:299px">
    <svg width="40" height="40" viewBox="0 0 40 40"><circle cx="20" cy="10" r="8" fill="#fff"/><path d="M4 38l16-16 16 16z" fill="#fff"/></svg>
    <h3>Resources</h3>
    <p>For Colorado families living in an area where there are few or no attachment and trauma competent clinicians</p>
    <span class="btn-out">Read More</span>
  </div>
  <div class="tile" style="left:600px;top:239px;width:600px;background:linear-gradient(120deg,#4f8a3a,#c99a7c 50%,#5aa0c8)" role="img" aria-label="Photo of a smiling family with two children outdoors"></div>
</section>
<div class="blog-title"><h2 class="display">DON'T MISS OUR BLOG</h2><div class="rule"></div></div>
<article class="card" style="left:62px"><div class="card-img" role="img" aria-label="Photo of a carer with an elderly couple outdoors" style="background:linear-gradient(135deg,#8fb36a,#d9c4a8)"></div><h4>Etiam accumsan purus magna, et viverra neque</h4><div class="meta">John Doe &nbsp;&nbsp; June 8, 2015</div><p>Nullam ut mauris vitae tortor sodales efficitur. Quisque ac orci ante. Proin sit amet turpis lobortis, imperdiet nisl ut, viverra lorem.</p><span class="btn-out">READ MORE</span></article>
<article class="card" style="left:330px"><div class="card-img" role="img" aria-label="Photo of a doctor talking with an elderly woman" style="background:linear-gradient(135deg,#e4e0d6,#b8c4c0)"></div><h4>Etiam accumsan purus magna, et viverra neque</h4><div class="meta">John Doe &nbsp;&nbsp; June 8, 2015</div><p>Nullam ut mauris vitae tortor sodales efficitur. Quisque ac orci ante. Proin sit amet turpis lobortis, imperdiet nisl ut, viverra lorem.</p><span class="btn-out">READ MORE</span></article>
<article class="card" style="left:596px"><div class="card-img" role="img" aria-label="Photo of a nurse embracing an elderly man" style="background:linear-gradient(135deg,#7ec0b8,#e8e4dc)"></div><h4>Etiam accumsan purus magna, et viverra neque</h4><div class="meta">John Doe &nbsp;&nbsp; June 8, 2015</div><p>Nullam ut mauris vitae tortor sodales efficitur. Quisque ac orci ante. Proin sit amet turpis lobortis, imperdiet nisl ut, viverra lorem.</p><span class="btn-out">READ MORE</span></article>
<article class="card" style="left:864px"><div class="card-img" role="img" aria-label="Photo of a therapist helping a senior with exercises" style="background:linear-gradient(135deg,#cfd8c2,#8a9a88)"></div><h4>Etiam accumsan purus magna, et viverra neque</h4><div class="meta">John Doe &nbsp;&nbsp; June 8, 2015</div><p>Nullam ut mauris vitae tortor sodales efficitur. Quisque ac orci ante. Proin sit amet turpis lobortis, imperdiet nisl ut, viverra lorem.</p><span class="btn-out">READ MORE</span></article>
<footer class="footer">
  <div class="brand-dot"></div>
  <div class="brand-name">VELNORA</div>
  <div class="footer-links"><span>Home</span>|<span>What We Do</span>|<span>Clinicians</span>|<span>About Wellness</span>|<span>About EMDR</span>|<span>Phone Coaching</span>|<span>Insurance</span>|<span>Resources</span>|<span>Contact Us</span></div>
  <div class="copy">Copyright © 2007 - 2015 velnoracare.com, Inc. All Rights Reserved</div>
  <div class="social"><i></i><i></i><i></i><i></i></div>
</footer>
</body>
</html>
```